" A empresa atua em dois segmentos: 1) atendimento psicológico de crianças, adolescentes e adultos e 2) recrutamento, seleçao e treinamento de pessoas. A proposta é trabalhar com o desenvolvimento humano em suas diversas dimensoes. "

```html
<!DOCTYPE html>
<html lang="pt-BR">
<head>
<meta charset="utf-8">
<title>Rumo Pleno – Pasta institucional</title>
<link rel="stylesheet" href="https://fonts.googleapis.com/css2?family=Exo+2:wght@400;500&display=swap">
<style>
  :root {
    --teal: #12aaa4;
    --teal-light: #4ec7c2;
    --paper: #ffffff;
    --mist: #e4e4e6;
    --flap: #6d6e70;
    --ink-gray: #6b6b6d;
    --stage: #ececec;
  }
  html, body {
    margin: 0;
    padding: 0;
    width: 1200px;
    height: 1200px;
    overflow: hidden;
    background: var(--stage);
  }
  .folder-spread {
    position: relative;
    width: 1200px;
    height: 1200px;
  }
  .folder-shapes {
    position: absolute;
    inset: 0;
  }
  .brand-block {
    position: absolute;
    left: 738px;
    top: 570px;
    font-family: "Exo 2", sans-serif;
  }
  .brand-name {
    margin: 0;
    font-size: 60px;
    font-weight: 500;
    line-height: 1;
    color: var(--teal);
    letter-spacing: 1px;
  }
  .brand-tagline {
    margin: 6px 0 0 2px;
    font-size: 25px;
    font-weight: 500;
    color: var(--ink-gray);
    letter-spacing: 2px;
  }
  .contact-block {
    position: absolute;
    left: 56px;
    top: 866px;
    font-family: "Exo 2", sans-serif;
    font-size: 13px;
    line-height: 17px;
    color: var(--paper);
  }
  .contact-block p { margin: 0; }
</style>
</head>
<body>
<main class="folder-spread">
  <svg class="folder-shapes" width="1200" height="1200" viewBox="0 0 1200 1200">
    <defs>
      <clipPath id="left-panel-clip"><rect x="40" y="140" width="560" height="840"/></clipPath>
      <clipPath id="right-panel-clip"><rect x="600" y="140" width="560" height="840"/></clipPath>
    </defs>

    <!-- pocket flap -->
    <path class="pocket-flap" fill="var(--flap)"
          d="M40 980 H640 V1010 Q640 1062 580 1062 H120 Q70 1062 52 1030 Q40 1008 40 980 Z"/>
    <path class="pocket-flap-tab" fill="var(--paper)"
          d="M40 980 Q40 1010 60 1024 Q40 1026 28 1010 Q20 990 40 980 Z"/>

    <!-- back panel (teal) and front panel (white) -->
    <rect class="panel-back" x="40" y="140" width="560" height="840" fill="var(--teal)"/>
    <rect class="panel-front" x="600" y="140" width="560" height="840" fill="var(--paper)"/>

    <!-- large soft circle across the spine -->
    <circle class="spread-circle" cx="582" cy="700" r="302" fill="var(--teal-light)" clip-path="url(#left-panel-clip)"/>
    <circle class="spread-circle" cx="582" cy="700" r="302" fill="var(--mist)" clip-path="url(#right-panel-clip)"/>

    <!-- binder holes -->
    <circle class="binder-hole" cx="600" cy="342" r="28" fill="none" stroke="#9a9a9a" stroke-width="1.5"/>
    <circle class="binder-hole" cx="600" cy="755" r="28" fill="none" stroke="#9a9a9a" stroke-width="1.5"/>

    <!-- brand dot -->
    <circle class="brand-dot" cx="928" cy="500" r="56" fill="var(--teal)"/>
  </svg>

  <div class="brand-block">
    <h1 class="brand-name">Rumo Pleno</h1>
    <p class="brand-tagline">Desenvolvimento Humano</p>
  </div>

  <address class="contact-block">
    <p>Rua das Acácias nº 210</p>
    <p>Campinas SP</p>
    <p>11 5555 0101</p>
    <p>11 5555 0202</p>
    <p>www.rumopleno.com.br</p>
  </address>
</main>
</body>
</html>
```